Harbrook Faith Broadcasting needs a marketing flyer.

We need a flyer that will be mailed to churches/ministries looking to place their Christian radio program on one or more of our 39 AM/FM radio stations. I have included a sample of our last flyer. Details to include: 4 Stations for $50.00 or 7 Stations for $70.00. www.HarbrookBroadcast.example. Call Marta today at 888-555-0147 or email Marta@HarbrookBroadcast.example. Guaranteed Rates for 2 Years. No Charge for FM Stations. List stations in the order you see them on the attached flyer. Under the stations make note of the following: *Tucson, Kansas City, Bakersfield, Richmond, Pittsburgh and Indianapolis not included in this offer due to considerable operating expenses. Call our corporate office for rate quotes. (Put a * beside these stations in the station list). Also, we want to mention that we have a mobile app and online streaming.

Target Market(s)

Churches/ministries

Font styles to use
Serif
Sans Serif

Colors

Designer to choose colors to be used in the design.

Requirements
Must have
• KPZR AM 1000 (KQVT AM 1190) Albuquerque, NM
• KHPJ AM 840 & FM 99.7 Alexandria, LA
• WQPN AM 1230 Asheville, NC
• WRJZ AM 1050 Augusta, GA
• *KQOB AM 1410 Bakersfield, CA
• WVTZ AM 1450 & FM 103.3 Chattanooga, TN
• WQZU AM 1360 & FM 104.3 Greenville, SC
• WQJM AM 1140 & FM 101.3 Huntsville, AL
• *WPZQ AM 1500 & FM 96.7 Indianapolis, IN
• *KVQJ AM 1380 & FM 96.1 Kansas City, MO
• WQVB AM 1270 & FM 97.9 Mobile, AL
• WZQP AM 540 & FM 106.1 Mobile, AL
• KPJZ AM 1560 & FM 101.5 Omaha, NE
• WQXH AM 1070 & FM 104.5 Pensacola, FL
• WZPB AM 610 & FM 105.3 Pensacola, FL
• *WQKJ AM 1080 Pittsburgh, PA
• *WQPB AM 1290 & FM 103.3 Richmond, VA
• KZQV AM 1480 & FM 94.9 Shreveport, LA
• *KVJQ AM 940 Tucson, AZ
• WZJQ AM 940 & FM 105.7 Tupelo, MS
• WQRZ AM 1250 & FM 98.1 York, PA
• WZQM AM 1550 & FM 94.7 WilkesBarre/Scranton, PA
Should not have
• Although we are Christian, we need the flyer to be more professional. There is no need for crosses and/or white doves, etc.

```html
<!DOCTYPE html>
<html lang="en">
<head>
<meta charset="utf-8">
<title>Harbrook Faith Broadcasting – Station Rates Flyer</title>
<link rel="stylesheet" href="https://fonts.googleapis.com/css2?family=Playfair+Display:wght@700;900&family=Oswald:wght@500;700&family=Open+Sans:wght@400;600;700&display=swap">
<style>
  :root {
    --red: #d3141c;
    --red-deep: #8e0a10;
    --black: #0b0b0c;
    --ink: #141416;
    --white: #ffffff;
    --grey: #c9c9c9;
    --sunset: #e0582a;
  }
  * { margin: 0; padding: 0; box-sizing: border-box; }
  html, body { width: 855px; height: 1200px; overflow: hidden; background: #e6e6e6; }
  .flyer {
    position: relative; width: 855px; height: 1200px; overflow: hidden;
    background: var(--black); color: var(--white);
    font-family: "Open Sans", Arial, sans-serif;
  }
  .hero-photo {
    position: absolute; left: 0; top: 0; width: 855px; height: 560px;
    background:
      radial-gradient(ellipse 60% 40% at 50% 20%, rgba(255,170,90,.75), rgba(255,120,60,0) 70%),
      linear-gradient(180deg, #3a1a1e 0%, #a8402c 22%, var(--sunset) 34%, #6b1419 52%, #2a0a0c 74%, var(--black) 100%);
  }
  .swoosh { position: absolute; left: 0; top: 0; width: 855px; height: 1200px; }
  .headline {
    position: absolute; top: 318px; left: 0; width: 855px; text-align: center;
    font-family: "Playfair Display", Georgia, serif; font-weight: 900;
    text-transform: uppercase; line-height: 1.05;
    text-shadow: 0 2px 6px rgba(0,0,0,.6);
  }
  .headline .line-1 { font-size: 36px; letter-spacing: .5px; }
  .headline .line-2 { font-size: 58px; letter-spacing: 1px; }
  .rates-hint {
    position: absolute; top: 425px; left: 0; width: 855px; text-align: center;
    font-family: "Oswald", sans-serif; font-weight: 500; font-size: 14px; letter-spacing: 1.5px;
  }
  .guarantee-badge {
    position: absolute; left: 78px; top: 448px; width: 150px; height: 150px;
    border-radius: 50%; background: var(--white);
    border: 5px solid var(--red);
    display: flex; align-items: center; justify-content: center;
    box-shadow: 0 4px 14px rgba(0,0,0,.6);
  }
  .guarantee-badge .ribbon {
    width: 168px; background: var(--red); color: var(--white);
    font-family: "Playfair Display", Georgia, serif; font-weight: 700;
    text-align: center; font-size: 17px; line-height: 1.1; padding: 7px 0;
    transform: rotate(-14deg);
  }
  .contact {
    position: absolute; top: 455px; left: 505px; width: 260px; text-align: center;
    font-family: "Playfair Display", Georgia, serif; font-weight: 700;
  }
  .contact .call { font-size: 20px; }
  .contact .phone { font-size: 19px; }
  .contact .or { font-size: 12px; font-family: "Open Sans", sans-serif; margin: 2px 0; }
  .contact .email { font-size: 14px; }
  .offer {
    position: absolute; top: 640px; font-family: "Oswald", sans-serif; font-weight: 700;
  }
  .offer .count { font-size: 34px; letter-spacing: 1px; display: block; padding-left: 42px; }
  .offer .price-row { display: flex; align-items: center; }
  .offer .for {
    font-size: 24px; writing-mode: vertical-rl; transform: rotate(180deg);
    width: 34px; margin-right: 8px; line-height: 1;
  }
  .offer .price { font-size: 58px; line-height: 1; }
  .offer-4 { left: 72px; }
  .offer-7 { left: 555px; }
  .offer-or {
    position: absolute; top: 635px; left: 0; width: 855px; text-align: center;
    font-family: "Oswald", sans-serif; font-weight: 700; font-size: 96px; line-height: 1;
  }
  .station-lists {
    position: absolute; top: 780px; left: 60px; width: 735px;
    display: flex; justify-content: space-between;
    font-size: 9.6px; line-height: 1.55; color: var(--grey);
  }
  .station-lists ul { list-style: none; width: 235px; }
  .station-lists li::before { content: "• "; color: var(--red); }
  .fine-print {
    position: absolute; top: 930px; left: 120px; width: 615px;
    border: 1px solid var(--red); padding: 10px 14px;
    font-size: 11px; line-height: 1.45; text-align: center; color: var(--white);
  }
  .footer-bar {
    position: absolute; top: 1048px; left: 0; width: 855px; height: 40px;
    background: var(--ink); border-top: 2px solid var(--red); border-bottom: 2px solid var(--red);
    display: flex; align-items: center; justify-content: space-around;
    font-size: 12px; font-weight: 600;
  }
  .footer-bar .item { display: flex; align-items: center; gap: 8px; }
  .icon-chip {
    width: 22px; height: 22px; border-radius: 4px; background: var(--red);
    display: flex; align-items: center; justify-content: center;
  }
  .services { position: absolute; top: 1102px; right: 70px; display: flex; gap: 34px; }
  .service { width: 70px; text-align: center; font-size: 9.5px; font-weight: 600; }
  .service .circle {
    width: 62px; height: 62px; margin: 0 auto 5px; border-radius: 50%;
    background: var(--white); border: 3px solid var(--red);
    display: flex; align-items: center; justify-content: center;
  }
</style>
</head>
<body>
<main class="flyer">
  <div class="hero-photo" role="img" aria-label="City skyline at sunset with a studio microphone standing above it, tinted red"></div>

  <svg class="swoosh" viewBox="0 0 855 1200" aria-hidden="true">
    <path d="M0 600 C 200 690 620 700 855 560 L855 760 L0 760 Z" fill="#120708" opacity=".85"/>
    <circle cx="428" cy="470" r="290" fill="none" stroke="var(--red)" stroke-width="5" stroke-dasharray="620 200" transform="rotate(120 428 470)"/>
    <path d="M0 700 C 220 640 600 640 855 720" fill="none" stroke="var(--red)" stroke-width="3" opacity=".7"/>
    <path d="M0 1005 C 260 960 600 980 855 1010 L855 1030 C 600 1000 260 985 0 1025 Z" fill="var(--red-deep)"/>
  </svg>

  <h1 class="headline">
    <span class="line-1">No charge for FM station and first</span><br>
    <span class="line-2">Month Free</span>
  </h1>
  <p class="rates-hint">SEE RATES BELOW FOR FM STATIONS</p>

  <div class="guarantee-badge"><div class="ribbon">Guaranteed Rates<br>for 2 Years</div></div>

  <div class="contact">
    <p class="call">Call Marta today at</p>
    <p class="phone">888-555-0147</p>
    <p class="or">OR EMAIL</p>
    <p class="email">Marta@HarbrookBroadcast.example</p>
  </div>

  <div class="offer offer-4">
    <span class="count">4 STATIONS</span>
    <div class="price-row"><span class="for">FOR</span><span class="price">$50.00</span></div>
  </div>
  <div class="offer-or">OR</div>
  <div class="offer offer-7">
    <span class="count">7 STATIONS</span>
    <div class="price-row"><span class="for">FOR</span><span class="price">$70.00</span></div>
  </div>

  <section class="station-lists">
    <ul>
      <li>KPZR AM 1000 (KQVT AM 1190) Albuquerque, NM</li>
      <li>KHPJ AM 840 &amp; FM 99.7 Alexandria, LA</li>
      <li>WQPN AM 1230 Asheville, NC</li>
      <li>WRJZ AM 1050 Augusta, GA</li>
      <li>*KQOB AM 1410 Bakersfield, CA</li>
      <li>WVTZ AM 1450 &amp; FM 103.3 Chattanooga, TN</li>
      <li>WQZU AM 1360 &amp; FM 104.3 Greenville, SC</li>
      <li>WQJM AM 1140 &amp; FM 101.3 Huntsville, AL</li>
    </ul>
    <ul>
      <li>*WPZQ AM 1500 &amp; FM 96.7 Indianapolis, IN</li>
      <li>*KVQJ AM 1380 &amp; FM 96.1 Kansas City, MO</li>
      <li>WQVB AM 1270 &amp; FM 97.9 Mobile, AL</li>
      <li>WZQP AM 540 &amp; FM 106.1 Mobile, AL</li>
      <li>KPJZ AM 1560 &amp; FM 101.5 Omaha, NE</li>
      <li>WQXH AM 1070 &amp; FM 104.5 Pensacola, FL</li>
      <li>WZPB AM 610 &amp; FM 105.3 Pensacola, FL</li>
    </ul>
    <ul>
      <li>*WQKJ AM 1080 Pittsburgh, PA</li>
      <li>*WQPB AM 1290 &amp; FM 103.3 Richmond, VA</li>
      <li>KZQV AM 1480 &amp; FM 94.9 Shreveport, LA</li>
      <li>*KVJQ AM 940 Tucson, AZ</li>
      <li>WZJQ AM 940 &amp; FM 105.7 Tupelo, MS</li>
      <li>WQRZ AM 1250 &amp; FM 98.1 York, PA</li>
      <li>WZQM AM 1550 &amp; FM 94.7 WilkesBarre/Scranton, PA</li>
    </ul>
  </section>

  <p class="fine-print">*Tucson, Kansas City, Bakersfield, Richmond, Pittsburgh and Indianapolis are not included in this offer due to considerable operating expenses. Call our corporate office for rate quotes.</p>

  <footer class="footer-bar">
    <div class="item">
      <span class="icon-chip"><svg width="14" height="10" viewBox="0 0 14 10"><rect x=".5" y=".5" width="13" height="9" fill="none" stroke="#fff"/><path d="M.5 .5 7 6 13.5 .5" fill="none" stroke="#fff"/></svg></span>
      Marta@HarbrookBroadcast.example
    </div>
    <div class="item">
      <span class="icon-chip"><svg width="14" height="14" viewBox="0 0 14 14"><circle cx="7" cy="7" r="6" fill="none" stroke="#fff"/><path d="M1 7h12M7 1c3 3 3 9 0 12M7 1c-3 3-3 9 0 12" fill="none" stroke="#fff"/></svg></span>
      www.HarbrookBroadcast.example
    </div>
    <div class="item">
      <span class="icon-chip"><svg width="12" height="12" viewBox="0 0 12 12"><path d="M2 1l2.5 0 1 3-1.5 1c.7 1.5 1.5 2.3 3 3l1-1.5 3 1V11C6 11 1 6 1 2z" fill="#fff"/></svg></span>
      888-555-0147
    </div>
  </footer>

  <div class="services">
    <div class="service">
      <div class="circle"><svg width="22" height="34" viewBox="0 0 22 34"><rect x="1.5" y="1.5" width="19" height="31" rx="3" fill="none" stroke="var(--red)" stroke-width="3"/><circle cx="11" cy="28" r="1.8" fill="var(--red)"/></svg></div>
      MOBILE APP
    </div>
    <div class="service">
      <div class="circle"><svg width="32" height="26" viewBox="0 0 32 26"><path d="M8 5a11 11 0 0 0 0 16M24 5a11 11 0 0 1 0 16M12 9a5 5 0 0 0 0 8M20 9a5 5 0 0 1 0 8" fill="none" stroke="var(--red)" stroke-width="2.6" stroke-linecap="round"/><circle cx="16" cy="13" r="2.4" fill="var(--red)"/></svg></div>
      ONLINE STREAMING
    </div>
  </div>
</main>
</body>
</html>
```